Rimah Advertising & Publicity business cards

I would like my Company's business card to be designed creatively & profissionally the logo is attached in both Arabic & english and prefer to have my emblem dimmed on the card as well
-Logo ( Arabic & English)
-Name (Arabic & English)
-Title ( Arabic & English)
-----------
-Location
-Landline (icon)
-Mobile phone (icon)
-Email (icon)
-Snapgram (icon)
-ChatLine (icon)

Target Market(s)

Industry/Entity Type

Marketing

Contact Information for Business Card

-Logo ( Arabic & English)
-Name (Arabic & English)
-----------
-Location
-Landline (icon)
-Mobile phone (icon)
-Email (icon)
-Snapgram (icon)
-ChatLine (icon)

Font styles to use
Serif

Requirements
Must have
• all what is mentions in business card details blanked and i will add the data my self
Nice to have
• Dim emblem on my business card both Arabic & english

```html
<!DOCTYPE html>
<html lang="en">
<head>
<meta charset="utf-8">
<title>Rimah Advertising &amp; Publicity – Business Card</title>
<link rel="stylesheet" href="https://fonts.googleapis.com/css2?family=Questrial&family=Roboto+Condensed:wght@300;400&display=swap">
<style>
  :root {
    --card-width: 1200px;
    --card-height: 702px;
    --panel-left-start: #e3e3e3;
    --panel-left-end: #f8f7ee;
    --teal: #45c2c0;
    --teal-light: #8fd5d2;
    --ink: #231f20;
    --ink-soft: #3b3b3b;
    --white: #ffffff;
    --slate: #6a6166;
    --icon-grey: #5c5c5c;
  }
  * { margin: 0; padding: 0; box-sizing: border-box; }
  html, body {
    width: var(--card-width);
    height: var(--card-height);
    overflow: hidden;
    background: var(--white);
  }
  .card {
    position: relative;
    width: var(--card-width);
    height: var(--card-height);
    display: flex;
  }
  .brand-panel {
    position: relative;
    width: 618px;
    height: 100%;
    background: linear-gradient(90deg, var(--panel-left-start) 0%, var(--panel-left-end) 100%);
  }
  .brand-mark {
    position: absolute;
    left: 84px;
    top: 296px;
    width: 108px;
    height: 108px;
    border-radius: 50%;
    background: var(--teal);
  }
  .brand-divider {
    position: absolute;
    left: 213px;
    top: 296px;
    width: 2px;
    height: 117px;
    background: var(--ink);
  }
  .brand-name {
    position: absolute;
    left: 228px;
    top: 282px;
    font-family: "Questrial", sans-serif;
    font-size: 92px;
    line-height: 1;
    color: var(--ink);
    letter-spacing: 1px;
  }
  .brand-tagline {
    position: absolute;
    left: 228px;
    top: 380px;
    font-family: "Questrial", sans-serif;
    font-size: 21.5px;
    color: var(--ink-soft);
  }
  .contact-panel {
    position: relative;
    flex: 1;
    height: 100%;
    background: radial-gradient(circle at 160px 300px, var(--teal-light) 0%, var(--teal) 65%);
    color: var(--white);
    font-family: "Roboto Condensed", sans-serif;
    font-weight: 300;
  }
  .person-name {
    position: absolute;
    left: 53px;
    top: 118px;
    font-size: 45px;
    font-weight: 400;
    line-height: 1;
  }
  .person-name .surname { color: var(--slate); }
  .contact-list { list-style: none; }
  .contact-item {
    position: absolute;
    left: 53px;
    display: flex;
    align-items: flex-start;
    font-size: 40px;
    line-height: 46px;
  }
  .contact-item svg { width: 44px; height: 44px; margin-right: 12px; flex: none; }
  .contact-item--phone { top: 221px; }
  .contact-item--mobile { top: 276px; }
  .contact-item--email { top: 331px; }
  .contact-item--address { top: 385px; }
  .social-list {
    position: absolute;
    left: 168px;
    top: 525px;
    display: flex;
    gap: 22px;
    list-style: none;
  }
  .social-item {
    display: flex;
    align-items: center;
    gap: 8px;
    font-size: 22px;
    font-weight: 400;
  }
  .social-dot {
    width: 38px;
    height: 38px;
    border-radius: 50%;
    background: var(--icon-grey);
  }
  .social-dot--outline { background: none; border: 3px solid var(--icon-grey); }
  .social-item--chat { color: var(--icon-grey); }
  .social-item--photos { color: var(--icon-grey); }
</style>
</head>
<body>
<div class="card">
  <section class="brand-panel">
    <div class="brand-mark"></div>
    <div class="brand-divider"></div>
    <div class="brand-name">Rimah</div>
    <div class="brand-tagline">Advertising and Publicity</div>
  </section>

  <section class="contact-panel">
    <h1 class="person-name">AlRashidi <span class="surname">Lastname</span></h1>
    <ul class="contact-list">
      <li class="contact-item contact-item--phone">
        <svg viewBox="0 0 44 44" aria-hidden="true"><circle cx="22" cy="22" r="20" fill="none" stroke="#fff" stroke-width="2.5"/><path d="M15 12c2-1 3 0 4 3l1 3c0 1-1 2-2 3 1 3 3 5 6 6 1-1 2-2 3-2l3 1c3 1 4 2 3 4-1 2-3 3-5 3-8-1-15-8-16-16 0-2 1-4 3-5z" fill="#fff"/></svg>
        <span>000.000.0000</span>
      </li>
      <li class="contact-item contact-item--mobile">
        <svg viewBox="0 0 44 44" aria-hidden="true"><circle cx="22" cy="22" r="20" fill="none" stroke="#fff" stroke-width="2.5"/><rect x="15" y="9" width="14" height="26" rx="2.5" fill="none" stroke="#fff" stroke-width="2.5"/><line x1="15" y1="29" x2="29" y2="29" stroke="#fff" stroke-width="2"/></svg>
        <span>000.000.0000</span>
      </li>
      <li class="contact-item contact-item--email">
        <svg viewBox="0 0 44 44" aria-hidden="true"><circle cx="22" cy="22" r="20" fill="none" stroke="#fff" stroke-width="2.5"/><rect x="10" y="14" width="24" height="16" fill="#fff"/><path d="M10 14l12 10 12-10" fill="none" stroke="#45c2c0" stroke-width="2"/></svg>
        <span>email@ email.com</span>
      </li>
      <li class="contact-item contact-item--address">
        <svg viewBox="0 0 44 44" aria-hidden="true"><circle cx="22" cy="22" r="20" fill="none" stroke="#fff" stroke-width="2.5"/><path d="M22 35c-6-8-9-12-9-17a9 9 0 0 1 18 0c0 5-3 9-9 17z" fill="#fff"/><circle cx="22" cy="18" r="3.5" fill="#45c2c0"/></svg>
        <span>123 Address Goes Here<br>City, State, Zip</span>
      </li>
    </ul>
    <ul class="social-list">
      <li class="social-item social-item--photos"><span class="social-dot"></span>Snapgram</li>
      <li class="social-item social-item--chat"><span class="social-dot social-dot--outline"></span>ChatLine</li>
    </ul>
  </section>
</div>
</body>
</html>
```